Redesign of Smart Watch Gift Voucher-SEE ATTACHED CURRENT DESIGN

I need to redesign my existing design using all same content and elements.

MY ENVISION: I invision more of a professional advertisement type of flyer/voucher. Imagine how Corvel.com would create a professionally looking flyer promoting the lumo or veno.

you can get many ideas about professional design by looking at some of corvels flyer designs :
https://www.findora-example.net/search?q=lumo+advertisment&mode=img&ref=a83kd02mzq7

stock photos are attached, you do not have to use them all, you can use some or none i am open to your designs using your own images if you want...just make sure the smartwatch looks black

DO NOT LEAVE ANY CONTENT OR ELEMENTS OUT ON MOCK UP PLEASE

SEE ATTACHED CURRENT DESIGN

I need to redesign my existing design using all same content and elements. DO NOT LEAVE ANY CONTENT OR ELEMENTS OUT ON MOCK UP PLEASE

Target Market(s)

B2B-you can get many ideas about professional design by looking at some of corvels flyer designs :

Industry/Entity Type

Marketing

Requirements
Must have
• I need to redesign my existing design using all same content and elements. DO NOT LEAVE ANY CONTENT OR ELEMENTS OUT ON MOCK UP PLEASE

Nice to have

Should not have

```html
<!DOCTYPE html>
<html lang="en">
<head>
<meta charset="utf-8">
<title>Smartwatch Reward Flyer</title>
<link rel="stylesheet" href="https://fonts.googleapis.com/css2?family=Anton&family=Montserrat:ital,wght@0,400;0,600;0,700;0,800;1,800;1,900&display=swap">
<style>
  :root{
    --red:#e11b22;
    --red-deep:#b8121a;
    --yellow:#fff200;
    --ink:#111111;
    --body:#555555;
    --panel:#e5e5e5;
    --paper:#ffffff;
    --bar:#333333;
    --stage:#ececec;
  }
  *{margin:0;padding:0;box-sizing:border-box}
  html,body{width:1200px;height:2295px;overflow:hidden;background:var(--stage)}
  .canvas{position:relative;width:1200px;height:2295px}
  .flyer{
    position:absolute;left:50px;top:435px;width:690px;height:893px;
    transform:scale(1.5942);transform-origin:0 0;
    background:var(--panel);overflow:hidden;
    font-family:"Montserrat",Arial,sans-serif;
    box-shadow:0 2px 6px rgba(0,0,0,.18);
  }
  .shapes{position:absolute;inset:0}
  .photo-athlete{
    position:absolute;left:250px;top:0;width:440px;height:330px;
    background:linear-gradient(135deg,#d4cec2 0%,#cfc8ba 30%,#2f6fd3 48%,#1f3d8a 60%,#c49a7a 72%,#d8d2c6 100%);
    clip-path:polygon(6% 0,100% 0,100% 100%,14% 100%,0 55%);
  }
  .photo-watches{
    position:absolute;left:365px;top:295px;width:320px;height:190px;
    background:linear-gradient(90deg,#f2b01e 0%,#2a2a2a 18%,#1a1a1a 30%,#22d3e6 42%,#1c1c1c 55%,#2b2b2b 68%,#38d63c 82%,#1a1a1a 100%);
    border-radius:18px;
    -webkit-mask:linear-gradient(#000 80%,transparent);
    mask:linear-gradient(#000 80%,transparent);
  }
  .enjoy{position:absolute;left:72px;top:62px;font-family:"Anton",Impact,sans-serif;font-size:116px;line-height:1;color:var(--red);letter-spacing:-1px}
  .brand-new{position:absolute;left:72px;top:181px;font-weight:700;font-size:22px;color:var(--red);letter-spacing:.5px}
  .smartwatch{position:absolute;left:71px;top:213px;font-weight:800;font-size:29px;color:var(--red);letter-spacing:.5px}
  .headline{position:absolute;left:70px;top:354px;font-weight:900;font-style:italic;font-size:22.5px;line-height:24.5px;color:var(--ink);text-transform:uppercase}
  .intro{position:absolute;left:72px;top:476px;width:240px;font-size:11px;line-height:13.5px;color:var(--body)}
  .features-title{position:absolute;left:70px;top:626px;font-weight:800;font-size:25px;color:var(--red)}
  .feature-list{position:absolute;top:666px;list-style:none}
  .feature-list.col-a{left:68px}
  .feature-list.col-b{left:201px}
  .feature-list li{display:flex;align-items:center;gap:7px;height:18px;font-weight:700;font-size:8.6px;color:var(--ink)}
  .feature-list svg{width:11px;height:11px;flex:none}
  .certificate{position:absolute;left:69px;top:810px;color:var(--yellow);font-weight:700}
  .certificate .label{font-size:16px;letter-spacing:.3px}
  .certificate .id{font-size:27px;color:var(--paper);line-height:1.05}
  .certificate .expires{font-size:16px}
  .certificate .expires span{color:var(--paper)}
  .tag-title{position:absolute;left:400px;top:535px;font-weight:900;font-style:italic;font-size:18px;color:var(--ink)}
  .tag-title em,.how-title em{color:var(--red)}
  .testimonial{position:absolute;left:378px;top:577px;width:300px;font-size:8.4px;line-height:11px;color:#333}
  .testimonial .mark{position:absolute;font-family:Georgia,serif;font-weight:900;font-size:26px;color:var(--ink);line-height:1}
  .testimonial .open{left:0;top:-6px}
  .testimonial .close{left:146px;top:22px}
  .testimonial p{padding-left:24px}
  .testimonial cite{display:block;padding-left:24px;font-weight:800;font-style:italic}
  .how-title{position:absolute;left:380px;top:623px;font-weight:900;font-style:italic;font-size:18.5px;color:var(--ink)}
  .how-copy{position:absolute;left:350px;top:662px;width:300px;font-size:8.3px;line-height:10.6px;color:#444;text-align:center}
  .how-copy b{color:var(--ink)}
  .cta{position:absolute;left:328px;top:770px;width:297px;height:44px;background:var(--yellow);text-align:center;padding-top:3px}
  .cta .lead{font-size:16.5px;color:#333;letter-spacing:.4px}
  .cta .action{font-size:12px;font-weight:800;color:var(--red)}
  .site{position:absolute;left:322px;top:826px;font-weight:800;font-size:13.5px;color:var(--red)}
  .terms{position:absolute;left:322px;top:845px;font-weight:700;font-size:9.3px;color:var(--ink)}
</style>
</head>
<body>
<svg width="0" height="0" style="position:absolute" aria-hidden="true">
  <symbol id="tick" viewBox="0 0 12 12">
    <circle cx="6" cy="6" r="6" fill="#e11b22"/>
    <path d="M3.2 6.2l2 2 3.8-4" fill="none" stroke="#fff" stroke-width="1.6" stroke-linecap="round" stroke-linejoin="round"/>
  </symbol>
</svg>
<div class="canvas">
  <article class="flyer">
    <svg class="shapes" viewBox="0 0 690 893" width="690" height="893" aria-hidden="true">
      <defs>
        <linearGradient id="certFill" x1="0" y1="0" x2="1" y2="1">
          <stop offset="0" stop-color="#d71920"/>
          <stop offset="1" stop-color="#b3111a"/>
        </linearGradient>
      </defs>
      <polygon points="0,262 345,262 690,300 690,440 0,460" fill="#ececec"/>
      <polygon points="372,470 690,440 690,893 295,893" fill="#ffffff"/>
      <polygon points="0,0 160,0 0,128" fill="#e11b22"/>
      <polygon points="0,208 346,208 306,262 0,262" fill="#fff200"/>
      <polygon points="0,808 305,832 296,893 0,893" fill="url(#certFill)"/>
      <polygon points="388,530 625,530 612,558 376,558" fill="#fff200"/>
      <polygon points="296,884 690,884 690,893 295,893" fill="#333333"/>
    </svg>

    <div class="photo-athlete" role="img" aria-label="Photo of a man in a blue shirt sitting on stairs checking his smartwatch and phone, with blue fitness icons arranged around him"></div>
    <div class="photo-watches" role="img" aria-label="Photo of three black-faced smartwatches with yellow, cyan and green bands"></div>

    <h1 class="enjoy">ENJOY</h1>
    <p class="brand-new">YOUR BRAND NEW</p>
    <p class="smartwatch">SMARTWATCH</p>

    <h2 class="headline">Tale contreal<br>or your te whitin<br>your new smart<br>litihness wateln</h2>

    <p class="intro">Congratulations, you have been rewarded with a Brand New Smart Fitness Watch shipped &nbsp;right to your door. Just pay shipping and handling. Your new Smart Fitness Watch has these features: sport mode, pedometer, distance, calorie, heart rate, blood pressure, stopwatch, sleep monitoring, phone locator, reminders, remote camera, an alarm clock and much more!</p>

    <h3 class="features-title">FEATURES</h3>
    <ul class="feature-list col-a">
      <li><svg><use href="#tick"/></svg>Pedometer</li>
      <li><svg><use href="#tick"/></svg>Calorie Counter</li>
      <li><svg><use href="#tick"/></svg>Blood Pressure Monitor</li>
      <li><svg><use href="#tick"/></svg>Sleep Monitoring</li>
      <li><svg><use href="#tick"/></svg>Reminders Feature</li>
      <li><svg><use href="#tick"/></svg>Alarm Clock</li>
    </ul>
    <ul class="feature-list col-b">
      <li><svg><use href="#tick"/></svg>Distance Tracker</li>
      <li><svg><use href="#tick"/></svg>Heart Rate Monitor</li>
      <li><svg><use href="#tick"/></svg>Stopwatch</li>
      <li><svg><use href="#tick"/></svg>Phone Locator</li>
      <li><svg><use href="#tick"/></svg>Remote Camera</li>
      <li><svg><use href="#tick"/></svg>Waterproof</li>
    </ul>

    <div class="certificate">
      <p class="label">CERTIFICATE ID</p>
      <p class="id">91772-89218</p>
      <p class="expires">Expires <span>10/03/2020</span></p>
    </div>

    <h3 class="tag-title">WHAT <em>OTHERS SAY</em></h3>
    <blockquote class="testimonial">
      <span class="mark open">&ldquo;</span>
      <p>Are you sure this is not a Norvia Orbit<br>Smartwatch in &nbsp;DISGUISE???? &nbsp;| love mine.</p>
      <cite>-Marcus T. Bayview, NJ</cite>
      <span class="mark close">&rdquo;</span>
    </blockquote>

    <h3 class="how-title">HOW CAN <em>WE DO THIS?</em></h3>
    <p class="how-copy">We have a couple retail partners that we team up with to " crowd purchase" huge shipping containers that hold 10's of thousands of electronic products at <b>80-90% off</b> retail. We simply pass our savings on to you as we do not profit from our electronic products. You are basically able to <b>"piggy back"</b> on our partnerships and buying power to get an attractive electronic premium for a fraction of the retail cost.</p>

    <div class="cta">
      <p class="lead">VIEW ALL THE DETAILS OF THIS</p>
      <p class="action">SPECIAL OFFER AND REDEEM ONLINE AT</p>
    </div>
    <p class="site">WWW.PERKSANDREWARDSHUB.COM</p>
    <p class="terms">*Terms and Conditions apply see website for details</p>
  </article>
</div>
</body>
</html>
```